Plakat-Design für Vermieter von Ferienwohnungen im Allgäu
Zielgruppe
Wir vermieten Ferienwohnungen im Allgäu.
www.gasthof-lindenblick.de
Aufgabenstellung
Das Schild (Querformat) sollte freundlich, ansprechend und modern sein. Größe 140x180 cm.
Es wird eine Begrüßung für den Gast, wenn er in die Tiefgarage fährt.
Text:
Herzlich Willkommen
in der Haus Birkenwinkel
Als Hintergrund können wir uns Berge, Landschaft oder ähnliches vorstellen.

```html
<!DOCTYPE html>
<html lang="de">
<head>
<meta charset="utf-8">
<title>Herzlich Willkommen – Haus Birkenwinkel</title>
<link rel="stylesheet" href="https://fonts.googleapis.com/css2?family=Barlow:wght@400;600;700&family=Kaushan+Script&display=swap">
<style>
  :root {
    --brand-red: #b01e23;
    --sun-yellow: #ffe600;
    --sun-orange: #f5a400;
    --sky-light: #e6ecf1;
    --sky-blue: #a9bfd2;
    --lake-blue: #5f86ab;
    --lake-deep: #3f6486;
    --deck-warm: #b07a44;
    --white: #ffffff;
  }
  html, body {
    margin: 0;
    padding: 0;
    width: 900px;
    height: 1200px;
    overflow: hidden;
    background: #ffffff;
  }
  .poster {
    position: relative;
    width: 900px;
    height: 1200px;
    overflow: hidden;
    font-family: "Barlow", Arial, sans-serif;
  }
  .poster__photo {
    position: absolute;
    inset: 0;
    background:
      radial-gradient(ellipse 260px 320px at 90px 1060px, rgba(240,170,80,0.75), rgba(240,170,80,0) 70%),
      linear-gradient(to bottom,
        var(--sky-light) 0%,
        var(--sky-blue) 30%,
        #c9d4de 52%,
        var(--lake-blue) 58%,
        var(--lake-deep) 80%,
        var(--deck-warm) 92%,
        #6e6f72 100%);
  }
  .logo {
    position: absolute;
    left: 48px;
    top: 52px;
    display: flex;
    align-items: center;
    gap: 10px;
  }
  .logo__dot {
    width: 34px;
    height: 34px;
    border-radius: 50%;
    background: var(--sun-orange);
  }
  .logo__name {
    font-family: "Barlow", Arial, sans-serif;
    font-weight: 600;
    font-size: 30px;
    color: var(--brand-red);
  }
  .welcome-band {
    position: absolute;
    left: 0;
    top: 0;
  }
  .welcome-band__herzlich {
    font-family: "Barlow", Arial, sans-serif;
    font-weight: 400;
    font-size: 74px;
    fill: var(--brand-red);
  }
  .welcome-band__willkommen {
    font-family: "Kaushan Script", cursive;
    font-size: 150px;
    fill: var(--brand-red);
  }
  .welcome-band__place {
    font-family: "Barlow", Arial, sans-serif;
    font-size: 42px;
    fill: var(--brand-red);
  }
  .welcome-band__place-name { font-weight: 700; }
  .claim {
    position: absolute;
    right: 28px;
    top: 878px;
    color: var(--white);
    font-size: 31px;
    line-height: 1.3;
    text-align: left;
  }
  .claim__line { display: block; font-weight: 400; letter-spacing: 0.5px; }
  .claim__strong { display: block; font-weight: 700; letter-spacing: 0.5px; }
</style>
</head>
<body>
<main class="poster">
  <div class="poster__photo" role="img" aria-label="Foto: Füße auf einer Liege am Steg, daneben eine leuchtende Laterne, Blick über einen ruhigen See mit Inseln unter Abendhimmel"></div>

  <div class="logo">
    <span class="logo__dot"></span>
    <span class="logo__name">Gasthof Lindenblick</span>
  </div>

  <svg class="welcome-band" width="900" height="460" viewBox="0 0 900 460">
    <defs>
      <radialGradient id="bandGlow" cx="0.45" cy="0.45" r="0.6">
        <stop offset="0" stop-color="#fffbe0"/>
        <stop offset="0.3" stop-color="var(--sun-yellow)"/>
        <stop offset="1" stop-color="var(--sun-orange)"/>
      </radialGradient>
    </defs>
    <polygon points="0,159 756,112 770,376 0,427" fill="url(#bandGlow)"/>
    <g transform="rotate(-3.6 400 270)">
      <text class="welcome-band__herzlich" x="452" y="245">Herzlich</text>
      <text class="welcome-band__willkommen" x="48" y="340">Willkommen</text>
      <text class="welcome-band__place" x="112" y="418">in der <tspan class="welcome-band__place-name">Haus Birkenwinkel</tspan></text>
    </g>
  </svg>

  <p class="claim">
    <span class="claim__line">Ihr persönlicher</span>
    <span class="claim__strong">ERHOLUNGSORT.</span>
  </p>
</main>
</body>
</html>
```